Breezeway Climate Business Card Design

Design new, 2 sides, business cards for a residential and light commercial heating, air conditioning contractor.

Target Market(s)

Homeowners, small businesses

Industry/Entity Type

Business

Contact Information for Business Card

Dominic Vasquerelli
Phone - 555-214-6837
Email
Address - PO box 618
Millbrook NJ 07999
Website - www.BreezewayClimateLLC.example

Requirements
Must have
• logo, company colors, standard size with no die cut, so I can use printhaven

```html
<!DOCTYPE html>
<html lang="en">
<head>
<meta charset="utf-8">
<title>Breezeway Climate Business Card</title>
<link href="https://fonts.googleapis.com/css2?family=Montserrat:wght@400;700&display=swap" rel="stylesheet">
<style>
  :root {
    --page-bg: #e9e6e2;
    --card-black: #0b0b0b;
    --glow-red: #7a1410;
    --glow-mid: #3a0806;
    --cream: #f3e2a6;
    --gold: #f2c14e;
    --white: #f4f4f4;
    --divider: #8a8a8a;
  }
  * { margin: 0; padding: 0; box-sizing: border-box; }
  html, body { width: 1200px; height: 913px; overflow: hidden; }
  body {
    background: var(--page-bg);
    font-family: "Montserrat", Arial, sans-serif;
    position: relative;
  }
  .card {
    position: absolute;
    width: 700px;
    height: 400px;
    border-radius: 4px;
    overflow: hidden;
    background: var(--card-black);
    box-shadow: 0 10px 24px rgba(0,0,0,0.25);
  }
  .card-front { left: 60px; top: 40px;
    background: radial-gradient(ellipse 300px 190px at 50% 50%, var(--glow-red) 0%, var(--glow-mid) 55%, var(--card-black) 100%);
  }
  .card-back { left: 440px; top: 473px;
    background: radial-gradient(ellipse 170px 110px at 50% 30%, var(--glow-red) 0%, var(--glow-mid) 55%, var(--card-black) 100%);
  }
  .brand-name {
    position: absolute; left: 0; right: 0;
    text-align: center;
    color: var(--cream);
    font-weight: 700;
    text-transform: uppercase;
    letter-spacing: 2px;
  }
  .card-front .brand-name { top: 175px; font-size: 42px; }
  .card-back .brand-name { top: 105px; font-size: 22px; letter-spacing: 1.5px; }
  .holder-name {
    position: absolute; left: 0; right: 0; top: 205px;
    text-align: center;
    font-size: 24px;
    color: var(--white);
  }
  .holder-name .surname { font-weight: 700; color: var(--gold); text-transform: uppercase; }
  .contact-block {
    position: absolute; left: 0; right: 0; top: 258px;
    display: flex; justify-content: center;
  }
  .address {
    text-align: right; color: var(--white); font-size: 16px; line-height: 26px;
    padding-right: 16px; border-right: 1px solid var(--divider);
  }
  .reach { padding-left: 16px; color: var(--gold); font-size: 16px; line-height: 26px; }
  .reach-line { display: flex; align-items: center; gap: 8px; }
  .reach-line svg { width: 14px; height: 14px; }
</style>
</head>
<body>
  <section class="card card-front">
    <div class="brand-name">Breezeway Climate</div>
  </section>

  <section class="card card-back">
    <div class="brand-name">Breezeway Climate</div>
    <div class="holder-name">Dominic <span class="surname">Vasquerelli</span></div>
    <div class="contact-block">
      <div class="address">PO box 618<br>Millbrook NJ 07999</div>
      <div class="reach">
        <div class="reach-line">
          <svg viewBox="0 0 16 16" aria-hidden="true"><circle cx="8" cy="8" r="7" fill="none" stroke="#f4f4f4" stroke-width="1.3"/><path d="M5.5 4.5l1.5 0 .6 1.8-.9.7a5 5 0 0 0 2.3 2.3l.7-.9 1.8.6v1.5c-3.5.2-6.2-2.5-6-6z" fill="#f4f4f4"/></svg>
          555-214-6837
        </div>
        <div class="reach-line">
          <svg viewBox="0 0 16 16" aria-hidden="true"><circle cx="8" cy="8" r="7" fill="none" stroke="#f4f4f4" stroke-width="1.3"/><ellipse cx="8" cy="8" rx="3" ry="7" fill="none" stroke="#f4f4f4" stroke-width="1"/><line x1="1" y1="8" x2="15" y2="8" stroke="#f4f4f4" stroke-width="1"/></svg>
          www.BreezewayClimateLLC.example
        </div>
      </div>
    </div>
  </section>
</body>
</html>
```